BrivaTrek Freight Services Business cards

Would like a very unique design catchy but professional for business cards. Please use log provided.Marlon WellsCeo and Founder TransCon Logistix Solutions1-888-913-3225mwells@tlsolutionsus.comwww.bfservicesco.com

```html
<!DOCTYPE html>
<html lang="en">
<head>
<meta charset="utf-8">
<title>BrivaTrek Freight Services – Business Card</title>
<link rel="stylesheet" href="https://fonts.googleapis.com/css2?family=Open+Sans:wght@300;400;600;700&display=swap">
<style>
  :root {
    --page-bg: #e4e1dc;
    --card-top: #f3f4f6;
    --card-top-shade: #e2e6ea;
    --navy: #1b3a78;
    --band-blue: #1f4b8e;
    --band-blue-deep: #163a74;
    --accent-red: #c81e28;
    --accent-red-deep: #a8141d;
    --band-text: #f1f3f7;
    --band-text-soft: #d3dbe8;
    --divider: rgba(255,255,255,0.45);
  }
  * { box-sizing: border-box; margin: 0; padding: 0; }
  html, body {
    width: 1200px; height: 970px; overflow: hidden;
    background: var(--page-bg);
    font-family: "Open Sans", Arial, sans-serif;
  }
  .card {
    position: absolute; left: 100px; top: 201px;
    width: 1000px; height: 567px;
    border-radius: 26px; overflow: hidden;
    background: linear-gradient(180deg, var(--card-top) 0%, var(--card-top-shade) 100%);
    box-shadow: 0 18px 40px rgba(0,0,0,0.18);
  }
  .brand {
    position: absolute; left: 0; right: 0; top: 120px;
    display: flex; align-items: center; justify-content: center; gap: 16px;
  }
  .brand-square {
    width: 30px; height: 30px; background: var(--navy);
  }
  .brand-name {
    color: var(--navy); font-weight: 700; font-size: 38px; letter-spacing: 0.5px;
  }
  .info-band {
    position: absolute; left: 0; right: 0; top: 323px; height: 173px;
    background: linear-gradient(180deg, var(--band-blue) 0%, var(--band-blue-deep) 100%);
  }
  .person {
    position: absolute; right: 536px; top: 48px; text-align: right;
  }
  .person-name {
    color: var(--band-text); font-size: 35px; font-weight: 300; letter-spacing: 0.5px; line-height: 1.1;
  }
  .person-name strong { font-weight: 600; }
  .person-title {
    color: var(--band-text-soft); font-size: 20px; font-weight: 400; margin-top: 10px; letter-spacing: 0.5px;
  }
  .band-divider {
    position: absolute; left: 497px; top: 30px; width: 1px; height: 120px; background: var(--divider);
  }
  .contact-list {
    position: absolute; left: 523px; top: 28px; list-style: none;
  }
  .contact-item {
    display: flex; align-items: center; gap: 14px;
    color: var(--band-text); font-size: 22px; height: 42px;
  }
  .contact-icon { width: 20px; height: 20px; flex: none; }
  .address-band {
    position: absolute; left: 0; right: 0; bottom: 0; height: 63px;
    background: linear-gradient(180deg, var(--accent-red) 0%, var(--accent-red-deep) 100%);
    display: flex; align-items: center; justify-content: center;
    color: var(--band-text-soft); font-size: 22px;
  }
</style>
</head>
<body>
  <div class="card">
    <div class="brand">
      <span class="brand-square"></span>
      <span class="brand-name">BrivaTrek Freight Services</span>
    </div>

    <div class="info-band">
      <div class="person">
        <div class="person-name">DUSTIN <strong>HARROW</strong></div>
        <div class="person-title">CEO AND FOUNDER</div>
      </div>
      <div class="band-divider"></div>
      <ul class="contact-list">
        <li class="contact-item">
          <svg class="contact-icon" viewBox="0 0 20 20" aria-hidden="true">
            <path fill="#d8262f" d="M2 7c0-2 3-4 8-4s8 2 8 4v1h-4V6.5c-1-.6-2.4-.9-4-.9s-3 .3-4 .9V8H2z"/>
            <path fill="#d8262f" d="M4 9h12l1 8H3z"/>
            <circle cx="10" cy="13" r="2" fill="#1f4b8e"/>
          </svg>
          1-888-472-6081
        </li>
        <li class="contact-item">
          <svg class="contact-icon" viewBox="0 0 20 20" aria-hidden="true">
            <rect x="2" y="4" width="16" height="12" fill="#d8262f"/>
            <path d="M2 4l8 7 8-7" fill="none" stroke="#1f4b8e" stroke-width="1.6"/>
          </svg>
          dharrow@bfservicesco.com
        </li>
        <li class="contact-item">
          <svg class="contact-icon" viewBox="0 0 20 20" aria-hidden="true">
            <g fill="none" stroke="#d8262f" stroke-width="1.5">
              <circle cx="10" cy="10" r="7.5"/>
              <ellipse cx="10" cy="10" rx="3.3" ry="7.5"/>
              <path d="M2.5 10h15M4 6h12M4 14h12"/>
            </g>
          </svg>
          www.bfservicesco.com
        </li>
      </ul>
    </div>

    <div class="address-band">2417 Maple Crest Ave, Atlanta, GA 30327</div>
  </div>
</body>
</html>
```